Need to create logo for Brightfold Works Ltd

We supply the above mention products all around NZ. Trading under the company name Brightfold Works Ltd.

Industry/Entity Type

It Company

Contact Information for Business Card

Brightfold Works Ltd. 0800519274 0214703952 Trevor@Salvana.co.nz contact Trevor MARSH
Suppliers of Salvana Louvres, Metalix Tru shutters, Railspan curtains,Glow Core outdoor heaters,Tyzell outdoor heaters

```html
<!DOCTYPE html>
<html lang="en">
<head>
<meta charset="utf-8">
<title>Brightfold Works Ltd — Business Card</title>
<link rel="stylesheet" href="https://fonts.googleapis.com/css2?family=Cinzel:wght@400;700&family=Open+Sans:wght@400;600&display=swap">
<style>
  :root {
    --navy: #0f2240;
    --navy-deep: #0a1a33;
    --navy-soft: #1d3456;
    --paper: #ffffff;
    --ink-muted: #5a6475;
    --rule: rgba(255,255,255,0.55);
    --backdrop: #e9e6e1;
  }
  * { box-sizing: border-box; margin: 0; padding: 0; }
  html, body {
    width: 1200px; height: 1023px; overflow: hidden;
    background: var(--backdrop);
  }
  .stage { position: relative; width: 1200px; height: 1023px; }
  .card {
    position: absolute;
    width: 560px; height: 320px;
    border-radius: 26px;
    overflow: hidden;
    box-shadow: 0 10px 30px rgba(0,0,0,0.18);
  }

  /* Front face */
  .card-front { left: 70px; top: 110px; background: var(--paper); }
  .front-band {
    position: absolute; left: 0; right: 0; bottom: 0; height: 132px;
    background: linear-gradient(120deg, var(--navy-soft), var(--navy));
  }
  .person { position: absolute; left: 44px; top: 44px; }
  .person-name {
    font-family: "Cinzel", serif; font-weight: 700;
    font-size: 30px; letter-spacing: 1px; color: var(--navy);
  }
  .person-role {
    font-family: "Open Sans", sans-serif; font-size: 14px;
    color: var(--ink-muted); margin-top: 2px;
  }
  .contacts {
    position: absolute; right: 40px; top: 44px;
    list-style: none;
    font-family: "Open Sans", sans-serif; font-size: 16px; color: var(--navy);
  }
  .contacts li { display: flex; align-items: center; gap: 10px; margin-bottom: 8px; }
  .contact-icon {
    width: 18px; height: 18px; border-radius: 4px; background: var(--navy);
    display: inline-flex; align-items: center; justify-content: center;
  }

  /* Back face */
  .card-back {
    left: 570px; top: 560px;
    background: linear-gradient(135deg, var(--navy-soft) 0%, var(--navy) 45%, var(--navy-deep) 100%);
    color: var(--paper);
  }
  .brand {
    position: absolute; left: 44px; top: 56px;
    display: flex; align-items: center; gap: 20px;
  }
  .brand-square { width: 74px; height: 74px; background: var(--paper); }
  .brand-name {
    font-family: "Cinzel", serif; font-weight: 400;
    font-size: 34px; letter-spacing: 1px; color: var(--paper);
  }
  .suppliers {
    position: absolute; left: 0; right: 0; top: 178px;
    display: flex; align-items: center; gap: 14px; padding-left: 44px;
  }
  .suppliers::before { content: ""; width: 150px; height: 1px; background: var(--rule); }
  .suppliers::after { content: ""; flex: 1; height: 1px; background: var(--rule); }
  .suppliers-label {
    font-family: "Open Sans", sans-serif; font-size: 12px;
    letter-spacing: 1.5px; text-transform: uppercase;
  }
  .product-list {
    position: absolute; left: 44px; right: 30px; top: 208px;
    font-family: "Open Sans", sans-serif; font-size: 14.5px; line-height: 1.7;
    letter-spacing: 0.6px;
  }
</style>
</head>
<body>
<main class="stage">

  <section class="card card-front" aria-label="Business card front">
    <div class="person">
      <p class="person-name">Trevor Marsh</p>
      <p class="person-role">Director</p>
    </div>
    <ul class="contacts">
      <li>
        <span class="contact-icon">
          <svg width="12" height="12" viewBox="0 0 24 24" fill="#fff"><path d="M6.6 10.8a15 15 0 0 0 6.6 6.6l2.2-2.2a1 1 0 0 1 1-.25 11.4 11.4 0 0 0 3.6.57 1 1 0 0 1 1 1V20a1 1 0 0 1-1 1A17 17 0 0 1 3 4a1 1 0 0 1 1-1h3.5a1 1 0 0 1 1 1c0 1.25.2 2.45.57 3.57a1 1 0 0 1-.25 1z"/></svg>
        </span>0800519274
      </li>
      <li>
        <span class="contact-icon">
          <svg width="12" height="12" viewBox="0 0 24 24" fill="#fff"><rect x="6" y="2" width="12" height="20" rx="2"/><rect x="8" y="5" width="8" height="11" fill="#0f2240"/></svg>
        </span>0214703952
      </li>
      <li>
        <span class="contact-icon">
          <svg width="12" height="12" viewBox="0 0 24 24" fill="none" stroke="#fff" stroke-width="2"><rect x="3" y="5" width="18" height="14"/><path d="M3 5l9 8 9-8"/></svg>
        </span>Trevor@Salvana.co.nz
      </li>
    </ul>
    <div class="front-band"></div>
  </section>

  <section class="card card-back" aria-label="Business card back">
    <div class="brand">
      <span class="brand-square"></span>
      <h1 class="brand-name">Brightfold Works Ltd.</h1>
    </div>
    <div class="suppliers"><span class="suppliers-label">Suppliers</span></div>
    <p class="product-list">
      Salvana Louvres | Metalix Tru Shutters | Railspan Curtains<br>
      Glow Core Outdoor Heaters | Tyzell Outdoor Heaters
    </p>
  </section>

</main>
</body>
</html>
```